Vantorra Dubai

I want picture about my project but I need it simple because I'll start the project in May but I want to make an advertising before opening the project the company is a concierge and elite service and vip services such as booking restaurants hotels and other services I'll send the logo

I want the picture suscribe the title of my project I want the advertisement to be words not hotel or cars pics

I attached some photos may help you to understand the project

Target Market(s)

High class people pepole age above 30 years it gives the high class service

Industry/Entity Type

Advertising

Font styles to use
Script

Requirements
Must have
• The picture should be simple and give the idea of work the company do to public
Nice to have
• I would like the advertising in the picture to be gold as the logo modern way
Should not have
• I don't want to use concierge words and elite is fine

```html
<!DOCTYPE html>
<html lang="en">
<head>
<meta charset="utf-8">
<title>Vantorra Dubai – Luxury Agency</title>
<link rel="stylesheet" href="https://fonts.googleapis.com/css2?family=Montserrat:wght@500;600&family=Lato:wght@400&display=swap">
<style>
  :root {
    --page: #ffffff;
    --panel: #1b1b1b;
    --gold: #bfa06a;
    --gold-bright: #cdae72;
    --ivory: #ffffff;
  }
  * { margin: 0; padding: 0; box-sizing: border-box; }
  html, body {
    width: 1200px;
    height: 1000px;
    overflow: hidden;
    background: var(--page);
  }
  .canvas {
    position: relative;
    width: 1200px;
    height: 1000px;
    background: var(--page);
  }
  .ad-panel {
    position: absolute;
    left: 35px;
    top: 17px;
    width: 1130px;
    height: 963px;
    background: var(--panel);
    overflow: hidden;
  }
  .brand {
    position: absolute;
    left: 103px;
    top: 48px;
    width: 414px;
    text-align: center;
    font-family: "Montserrat", sans-serif;
    font-weight: 500;
    color: var(--gold-bright);
  }
  .brand-name {
    display: block;
    font-size: 52px;
    line-height: 1;
    letter-spacing: 0.16em;
    text-transform: uppercase;
  }
  .brand-place {
    display: block;
    margin-top: 12px;
    font-size: 22px;
    letter-spacing: 0.2em;
    text-transform: uppercase;
  }
  .tagline {
    position: absolute;
    left: 105px;
    top: 158px;
    font-family: "Montserrat", sans-serif;
    font-weight: 500;
    font-size: 40px;
    font-variant: small-caps;
    letter-spacing: 0.06em;
    color: var(--ivory);
  }
  .service-arc {
    position: absolute;
    left: 0;
    top: 0;
    width: 1130px;
    height: 963px;
  }
  .service-arc text {
    font-family: "Montserrat", sans-serif;
    font-weight: 500;
    font-size: 34px;
    font-variant: small-caps;
    letter-spacing: 0.06em;
    text-anchor: middle;
    dominant-baseline: middle;
  }
  .service-arc .light { fill: var(--ivory); }
  .service-arc .gold { fill: var(--gold); }
  .butler-photo {
    position: absolute;
    left: 520px;
    top: 498px;
    width: 610px;
    height: 465px;
    background: radial-gradient(ellipse at 52% 42%, #e6e6e6 0%, #a9a9a9 28%, #4a4a4a 55%, var(--panel) 78%);
  }
  .contact {
    position: absolute;
    left: 50px;
    top: 894px;
    font-family: "Lato", sans-serif;
    font-weight: 400;
    font-size: 31px;
    color: var(--gold);
  }
</style>
</head>
<body>
<main class="canvas">
  <section class="ad-panel">
    <div class="brand">
      <span class="brand-name">Vantorra</span>
      <span class="brand-place">Dubai</span>
    </div>
    <h1 class="tagline">Luxury Agency</h1>

    <svg class="service-arc" viewBox="0 0 1130 963" aria-label="Services">
      <text class="light" transform="translate(262 723) rotate(-90)">Yachts</text>
      <text class="gold" transform="translate(286 556) rotate(-78)">Villas</text>
      <text class="light" transform="translate(371 398) rotate(-58)">Rentals</text>
      <text class="gold" transform="translate(518 268) rotate(-33)">Marina One</text>
      <text class="light" transform="translate(677 282) rotate(-15)">Security Service</text>
      <text class="gold" transform="translate(995 296) rotate(25)">Limousines</text>
      <text class="light" transform="translate(331 640) rotate(-90)">Jets</text>
      <text class="gold" transform="translate(415 455) rotate(-60)">VIP Service</text>
    </svg>

    <div class="butler-photo" role="img" aria-label="White-gloved hand presenting a silver service bell, black tailcoat sleeve with cufflink"></div>

    <p class="contact">contact@vantorra-services.com</p>
  </section>
</main>
</body>
</html>
```